The Bayfield Wellness Clinic - Practice Flyer

We need a flyer that generally advertises our services. I've uploaded one old flyer as well as examples of others. I like the style of the materials made by this practice: https://www.facebook.com/PineRidgeCounselingHouse

```html
<!DOCTYPE html>
<html lang="en">
<head>
<meta charset="utf-8">
<title>The Bayfield Wellness Clinic – Practice Flyer</title>
<link rel="stylesheet" href="https://fonts.googleapis.com/css2?family=Open+Sans:wght@400;600&family=Playfair+Display:wght@400;700&display=swap">
<style>
  :root {
    --page-bg: #b9c18a;
    --sheet: #cfdcc0;
    --corner: #959f68;
    --strip: #e4e7dc;
    --photo-top: #97915e;
    --photo-mid: #7a6446;
    --photo-bottom: #45392b;
    --ink: #1c241b;
    --brand: #2f3b2b;
    --leaf: #8db63c;
    --leaf-dark: #2f7a3c;
    --rule: #9fbf55;
    --gold: #e6cd82;
    --icon-bg: #e9ebe2;
    --serif: "Playfair Display", Georgia, serif;
    --sans: "Open Sans", Arial, sans-serif;
  }
  * { box-sizing: border-box; margin: 0; padding: 0; }
  html, body { width: 1138px; height: 1200px; overflow: hidden; }
  body { background: var(--page-bg); position: relative; }

  .flyer {
    position: absolute; left: 161px; top: 20px;
    width: 815px; height: 1160px;
    background: var(--sheet);
    color: var(--ink);
    overflow: hidden;
  }
  .flyer__shapes { position: absolute; inset: 0; }

  .brand {
    position: absolute; left: 60px; top: 66px; width: 430px;
    display: flex; align-items: center; gap: 14px;
    font-family: var(--serif); font-weight: 700; color: var(--brand);
    font-size: 31px; line-height: 1.12;
  }
  .brand__dot { flex: none; width: 20px; height: 20px; border-radius: 50%; background: var(--corner); }

  .intro {
    position: absolute; left: 60px; top: 208px; width: 660px;
    font-family: var(--serif); font-size: 21px; line-height: 25px; font-weight: 400;
  }

  .divider { position: absolute; left: 230px; width: 82px; height: 38px; }
  .divider__mark {
    position: absolute; left: 17px; top: 0; width: 48px; height: 32px;
    border-radius: 50% 50% 40% 40% / 60% 60% 40% 40%;
    background: linear-gradient(90deg, var(--leaf-dark), var(--leaf));
  }
  .divider__rule { position: absolute; left: 0; bottom: 0; width: 82px; height: 2px; background: var(--rule); }
  .divider--first { top: 339px; }
  .divider--second { top: 897px; }

  .lead {
    position: absolute; font-family: var(--sans); font-weight: 600;
    font-size: 13.5px; line-height: 18.5px;
  }
  .lead--conditions { left: 60px; top: 409px; width: 585px; }
  .lead--method { left: 53px; top: 633px; width: 515px; }

  .bullets {
    position: absolute; list-style: none;
    font-family: var(--sans); font-size: 12.6px; line-height: 20.8px; letter-spacing: 0.2px;
  }
  .bullets li { position: relative; padding-left: 17px; white-space: nowrap; }
  .bullets li::before {
    content: ""; position: absolute; left: 1px; top: 7px;
    width: 7px; height: 4px; border-radius: 0 100% 0 100%;
    background: var(--leaf); transform: rotate(-40deg);
  }
  .bullets--left { left: 60px; top: 452px; }
  .bullets--right { left: 353px; top: 452px; }
  .bullets--treatments { left: 60px; top: 697px; }

  .contact { position: absolute; left: 60px; top: 968px; }
  .contact__name { font-family: var(--serif); font-weight: 700; font-size: 19px; line-height: 24px; }
  .contact__role { font-family: var(--sans); font-size: 12.5px; line-height: 17px; letter-spacing: 0.2px; }
  .contact__license { margin-top: 8px; font-family: var(--sans); font-size: 12.5px; line-height: 15.5px; letter-spacing: 0.2px; }
  .contact__phone, .contact__web { font-family: var(--serif); font-weight: 700; font-size: 19.5px; line-height: 26px; }
  .contact__phone { margin-top: 10px; }

  .social { position: absolute; left: 578px; top: 1024px; width: 196px; text-align: center; }
  .social__label { font-family: var(--serif); font-weight: 700; font-size: 23.5px; color: var(--gold); }
  .social__links { display: flex; justify-content: center; gap: 14px; margin-top: 12px; }
  .social__link { width: 42px; height: 42px; border-radius: 50%; background: var(--icon-bg); display: block; }
</style>
</head>
<body>
  <main class="flyer">
    <svg class="flyer__shapes" width="815" height="1160" viewBox="0 0 815 1160">
      <defs>
        <linearGradient id="photo-tone" x1="0" y1="0" x2="0" y2="1">
          <stop offset="0" stop-color="var(--photo-top)"/>
          <stop offset="0.5" stop-color="var(--photo-mid)"/>
          <stop offset="1" stop-color="var(--photo-bottom)"/>
        </linearGradient>
      </defs>
      <polygon class="corner-band" points="510,0 815,0 815,204" fill="var(--corner)"/>
      <g class="corner-rules" stroke="var(--strip)" stroke-width="1.5">
        <line x1="668" y1="70" x2="787" y2="70"/>
        <line x1="689" y1="76" x2="766" y2="76"/>
      </g>
      <polygon class="edge-strip" points="815,208 815,1160 456,1160" fill="var(--strip)"/>
      <polygon class="photo-panel" role="img" aria-label="Photo of a couple holding hands walking along a beach at sunset" points="815,216 815,1160 492,1160" fill="url(#photo-tone)"/>
    </svg>

    <div class="brand">
      <span class="brand__dot"></span>
      <span class="brand__name">The Bayfield Wellness Clinic</span>
    </div>

    <p class="intro">The Bayfield Wellness Clinic of Greater Harborview, (BWC) provides expert clinical care for anxiety disorders, obsessive compulsive and related disorders, and neuro developmental disorders in children, adolescents, and adults.</p>

    <div class="divider divider--first" role="img" aria-label="Small lotus ornament">
      <span class="divider__mark"></span><span class="divider__rule"></span>
    </div>

    <p class="lead lead--conditions">BWC proudly provides the Greater Harborview community with state-of-the-art assessment and evidence-based therapy for disorders including:</p>

    <ul class="bullets bullets--left">
      <li>Obsessive Compulsive Disorder</li>
      <li>Trichotillomania</li>
      <li>Excoriation Disorder</li>
      <li>Generalized Anxiety Disorder</li>
      <li>Panic Disorder</li>
      <li>Specific Phobias</li>
      <li>Hoarding Disorder</li>
    </ul>
    <ul class="bullets bullets--right">
      <li>Body Dysmophic Disorder</li>
      <li>Tic Disorders</li>
      <li>ADHD</li>
      <li>Learning Disorders</li>
      <li>Insomnia</li>
      <li>Social Anxiety Disorder</li>
    </ul>

    <p class="lead lead--method">BWC clinicians are highly trained in cognitive behavioral therapy (CBT), which included scientifically informed techniques that are tailored to each client’s unique needs.</p>

    <ul class="bullets bullets--treatments">
      <li>Treatments We Provide:</li>
      <li>Cognitive Behavioral Therapy (CBT)</li>
      <li>Exposure and Response Prevention(E/RP)</li>
      <li>Comprehensive Behavioral (ComB)/Habit Reversal Traning(HRT)</li>
      <li>Cognitive Behavioral Intervention for Tics(CBIT)</li>
      <li>Acceptance and Commitment Therapy(ACT)</li>
      <li>Organizational Skills Training(OST)</li>
      <li>CBT for Insomania(CBT-I)</li>
    </ul>

    <div class="divider divider--second" role="img" aria-label="Small lotus ornament">
      <span class="divider__mark"></span><span class="divider__rule"></span>
    </div>

    <div class="contact">
      <p class="contact__name">Elena R. Marsh, PsyD</p>
      <p class="contact__role">Executive Director Liscensed Clinical Psychologist</p>
      <p class="contact__license">New Jersey Lic. No. 35S10092417<br>Pennsylvania Lic. No. PS0184362</p>
      <p class="contact__phone">Tel:(555) 014-2286</p>
      <p class="contact__web">www.BayfieldWellnessClinic.com</p>
    </div>

    <div class="social">
      <p class="social__label">Find us on:</p>
      <div class="social__links">
        <span class="social__link" role="img" aria-label="Social page"></span>
        <span class="social__link" role="img" aria-label="Video channel"></span>
        <span class="social__link" role="img" aria-label="News feed"></span>
      </div>
    </div>
  </main>
</body>
</html>
```